Roofing Company needs YOU to help put us on top!

Brindlecrest Roofing, a fresh new company with quality and Innovation in mind, needs your help to stand out in the competitive Chicago market. With over 30 years of experience, all the right people and tools for the job, the only thing we are missing is your creative ideas in web design to help us grow our online presence.
Our Company offers exceptional quality at reasonable prices, we work for the everyday people both blue collar and white collar.

We have used MakerHarbor in the past with multiple successful campaigns, we are excited to see what you can come up with for our website.

www.BrindlecrestRoofing-demo.net will be the domain

We will be hiring a photographer for visual content on our pages later. Stock photos are okay to use but should follow theme.

Thank you for taking the time on the submissions, if you have any questions don't hesitate to ask and we will provide whatever is needed to you.

Target Market(s)

Homeowners & Commercial Clients between 21-65

Industry/Entity Type

Roofing

Coding

Coded - Design and coding required

Number of Pages Required

4 page

Font styles to use
Sans Serif

Colors
ffffff
ec1f27
000000
5c5c5c
757575
b2b2b2

Requirements
Must have
• Color Scheme - should follow around our logo
• As for pages we were looking for an About, Services, Projects (gallery page) and Contact.
• Main page please include social media links and a a place so people could use coinwell to make payments
• Website should work on desktop as well as mobile platforms
Nice to have
• A Live chat feature would be nice if possible
Should not have
• Obscure Colors or Common web templates

```html
<!DOCTYPE html>
<html lang="en">
<head>
<meta charset="utf-8">
<title>Brindlecrest Roofing</title>
<link href="https://fonts.googleapis.com/css2?family=Michroma&family=Open+Sans:ital,wght@0,400;0,600;0,700;1,400&display=swap" rel="stylesheet">
<style>
:root{
  --red:#ec1f27;
  --black:#000000;
  --ink:#1c1c1c;
  --grey-dark:#5c5c5c;
  --grey:#757575;
  --grey-light:#b2b2b2;
  --white:#ffffff;
  --footer:#161616;
  --footer-bottom:#0c0c0c;
}
*{box-sizing:border-box;margin:0;padding:0}
html,body{width:1200px;height:3077px;overflow:hidden}
body{position:relative;background:var(--white);font-family:"Open Sans",Arial,sans-serif;color:var(--grey-dark)}
.abs{position:absolute}
.heading{font-family:"Michroma","Open Sans",sans-serif;font-weight:400;color:var(--ink)}
.heading em{font-style:normal;color:var(--red)}
.title-rule{display:block;width:46px;height:3px;background:var(--red);margin:14px auto 0}

/* hero */
.hero{left:0;top:0;width:1200px;height:564px;background:linear-gradient(160deg,#3d6fb3 0%,#7fa8d8 35%,#c9d9ea 50%,#c99a62 66%,#9c6a3a 100%)}
.topbar{left:0;top:0;width:1200px;height:72px;background:var(--red)}
.topbar span{position:absolute;top:12px;color:var(--white);font-size:11px}
.nav{left:164px;top:41px;width:872px;height:66px;background:var(--white);box-shadow:0 2px 8px rgba(0,0,0,.15)}
.brand{left:38px;top:18px;display:flex;align-items:center;gap:10px}
.brand i{width:22px;height:22px;background:var(--red);display:block}
.brand b{font-family:"Michroma",sans-serif;font-weight:400;font-size:17px;color:var(--ink)}
.nav a{position:absolute;top:24px;font-size:13px;color:#333;text-decoration:none;font-weight:600}
.nav a.active{color:var(--ink);font-weight:700}
.nav a.active::after{content:"";position:absolute;left:-8px;right:-8px;top:38px;height:3px;background:var(--ink)}
.nav .sep{position:absolute;top:25px;width:1px;height:16px;background:#ddd}
.cta{left:708px;top:281px;width:332px;height:170px;background:rgba(20,20,20,.82);border-radius:4px;text-align:center;padding-top:26px}
.cta h1{font-family:"Open Sans",sans-serif;font-weight:600;color:var(--white);font-size:25px;line-height:34px}
.btn{display:inline-block;background:var(--red);color:var(--white);font-size:11px;font-weight:700;border-radius:3px}
.cta .btn{margin-top:20px;padding:10px 22px}
.dots{left:558px;top:521px;display:flex;gap:10px;align-items:center}
.dots span{width:10px;height:10px;border-radius:50%;background:var(--white)}
.dots span.on{width:30px;border-radius:5px;background:var(--red)}

/* about */
.about-photo{left:164px;top:621px;width:314px;height:220px;background:linear-gradient(135deg,#c95a3d,#e0806a 45%,#8a4b3a);border:5px solid #e4e4e4}
.about-text{left:498px;top:608px;width:540px}
.about-text h2{font-size:29px;text-align:left}
.about-text .title-rule{margin:10px 0 0}
.about-text p{margin-top:14px;font-size:11.5px;line-height:22px;color:var(--grey-dark)}
.about-text .btn{margin-top:16px;padding:10px 26px}
.divider{left:164px;top:898px;width:872px;height:1px;background:#ececec}

/* services */
.section-title{left:0;width:1200px;text-align:center;font-size:29px}
.ring{left:451px;top:1036px;width:257px;height:257px;border-radius:50%;border:2px solid var(--red)}
.ring-inner{left:471px;top:1056px;width:217px;height:217px;border-radius:50%;background:#efefef;border:10px solid #f7f7f7;display:flex;align-items:center;justify-content:center;gap:8px}
.ring-inner i{width:20px;height:20px;background:var(--red);display:block}
.ring-inner b{font-family:"Michroma",sans-serif;font-weight:400;font-size:14px;color:var(--ink)}
.service{width:270px}
.service h3{font-size:15px;font-weight:700;color:var(--ink)}
.service p{font-size:11px;line-height:17px;color:var(--grey);margin-top:5px}
.service.left{text-align:right;left:155px}
.service.right{left:769px}
.connector{width:24px;height:1px;background:var(--red)}
.connector::after{content:"";position:absolute;top:-3px;width:7px;height:7px;border-radius:50%;background:var(--red)}
.connector.l::after{right:-4px}
.connector.r::after{left:-4px}
.view-all{left:0;top:1300px;width:1200px;text-align:center;color:var(--red);font-weight:700;font-size:15px}

/* projects */
.projects{left:0;top:1374px;width:1200px;height:677px;background:linear-gradient(180deg,#bfc7bb,#d9dcd6 40%,#c8ccc6)}
.projects-veil{left:0;top:1374px;width:1200px;height:677px;background:rgba(255,255,255,.55)}
.tabs{left:162px;top:1512px;width:874px;height:57px;background:var(--white);box-shadow:0 2px 6px rgba(0,0,0,.12);display:flex;justify-content:space-around;align-items:center;padding:0 12px}
.tabs span{font-size:12px;color:#333;position:relative}
.tabs span.on{color:var(--red)}
.tabs span.on::before{content:"";position:absolute;left:-4px;right:-4px;top:-21px;height:3px;background:var(--red)}
.tile{overflow:hidden}
.tile .cap{position:absolute;left:0;right:0;bottom:0;height:30px;background:rgba(0,0,0,.6);color:var(--white);font-size:12px;text-align:center;line-height:30px}
.tile.feature{background:linear-gradient(180deg,#3b3f4c,#5a4c52 60%,#7c2a2a)}
.tile.feature::after{content:"";position:absolute;inset:0;background:rgba(20,20,30,.55)}
.tile.feature .label{position:absolute;left:0;right:0;top:118px;text-align:center;color:var(--white);font-size:21px;font-weight:600;z-index:2}
.tile.feature .zoom{position:absolute;left:198px;top:66px;width:34px;height:34px;background:var(--red);z-index:2;border-radius:3px}

/* testimonials */
.testimonials{left:0;top:2051px;width:1200px;height:375px;background:linear-gradient(180deg,#1e1f1d,#2b2d28 50%,#161614)}
.avatar{border-radius:50%;background:linear-gradient(180deg,#a58a76,#6d5a4d)}
.avatar.on{border:4px solid var(--white)}
.arrow{color:#ccc;font-size:22px}
.quote{left:185px;top:2282px;width:830px;text-align:center;color:#e6e6e6;font-style:italic;font-size:12px;line-height:22px}
.quote-mark{font-family:Georgia,serif;font-size:46px;color:#aaa;line-height:1}
.author{left:0;top:2356px;width:1200px;text-align:center;color:var(--white);font-weight:700;font-size:15px}

/* partners */
.strip{left:162px;top:2585px;width:874px;height:92px;background:linear-gradient(180deg,#fafafa,#e2e2e2);box-shadow:0 10px 18px rgba(0,0,0,.12)}
.strip-shadow{left:200px;top:2680px;width:800px;height:20px;background:radial-gradient(ellipse at top,rgba(0,0,0,.12),transparent 70%)}
.partner{background:#8a8a8a}

/* footer */
.footer{left:0;top:2769px;width:1200px;height:246px;background:var(--footer)}
.footer h4{font-size:13.5px;color:var(--white);font-weight:700}
.col{top:2805px}
.col ul{list-style:none;margin-top:18px}
.col li{font-size:11px;color:#ddd;line-height:28px}
.col li::before{content:"›";color:#aaa;margin-right:8px}
.contact-line{display:flex;gap:12px;font-size:11px;color:#ddd;line-height:16px;margin-top:12px}
.contact-line svg{flex:none;margin-top:1px}
.field{position:absolute;left:609px;width:181px;border:1px solid #3a3a3a;background:#1d1d1d;font-size:9.5px;color:#777;padding:4px 8px}
.submit{left:609px;top:2955px;width:80px;height:24px;background:var(--red);color:var(--white);font-size:10px;font-weight:700;text-align:center;line-height:24px}
.sub-copy{left:850px;top:2844px;width:190px;font-size:11px;line-height:16px;color:#ddd}
.sub-copy span{color:#888;display:block;margin-top:8px}
.sub-input{left:850px;top:2933px;width:149px;height:24px;background:var(--white)}
.sub-go{left:999px;top:2933px;width:37px;height:24px;background:var(--red);color:var(--white);font-size:10px;font-weight:700;text-align:center;line-height:24px}
.bottombar{left:0;top:3015px;width:1200px;height:62px;background:var(--footer-bottom)}
.copyright{left:162px;top:3037px;font-size:10.5px;color:#ccc}
.social{top:3032px;width:22px;height:22px;background:#3a3a3a}
</style>
</head>
<body>

<!-- Hero -->
<div class="abs hero" role="img" aria-label="Roofer in a hard hat hammering roof framing under a blue sky"></div>
<div class="abs topbar">
  <span style="left:718px">Email : info@brindlecrest-demo.net</span>
  <span style="left:927px">Phone : 312-555-0148</span>
</div>
<nav class="abs nav">
  <div class="abs brand"><i></i><b>Brindlecrest Roofing</b></div>
  <a class="active" style="left:406px">Home</a>
  <span class="sep" style="left:460px"></span>
  <a style="left:467px">About Us</a>
  <span class="sep" style="left:555px"></span>
  <a style="left:562px">Services</a>
  <span class="sep" style="left:640px"></span>
  <a style="left:653px">Our Projects</a>
  <span class="sep" style="left:758px"></span>
  <a style="left:772px">Contact Us</a>
</nav>
<div class="abs cta">
  <h1>When it comes to Your<br>home, Think Brindlecrest!</h1>
  <span class="btn">&#9998;&nbsp; Request A Quote</span>
</div>
<div class="abs dots"><span></span><span></span><span class="on"></span><span></span></div>

<!-- About -->
<div class="abs about-photo" role="img" aria-label="Workers fixing red metal roof sheets with a drill"></div>
<div class="abs about-text">
  <h2 class="heading">About <em>Brindlecrest Roofing</em></h2>
  <span class="title-rule"></span>
  <p>Lorem Ipsum is simply dummy text of the printing and typesetting industry. Lorem Ipsum has been the industry's standard dummy text ever since the 1500s, when an unknown printer took a galley of type and scrambled it to make a type specimen book. It has survived not only five centuries, but also the leap into electronic typesetting, remaining essentially unchanged. It was popularised in the 1960s with the release of Letraset sheets containing Lorem Ipsum passages. text ever since the 1500s, when an unknown printer. It has survived not only five centuries, but also the leap into electronic typesetting.</p>
  <span class="btn">Read More</span>
</div>
<div class="abs divider"></div>

<!-- Services -->
<h2 class="abs heading section-title" style="top:944px">Our <em>Services</em></h2>
<span class="abs title-rule" style="left:577px;top:990px;margin:0"></span>
<div class="abs ring"></div>
<div class="abs ring-inner"><i></i><b>Brindlecrest</b></div>

<div class="abs service left" style="top:1056px"><h3>Shingle Roofs</h3><p>Lorem Ipsum is simply dummy text of then of<br>printing and typesetting industry. Lorem</p></div>
<div class="abs service left" style="top:1136px"><h3>Kitchens And Baths</h3><p>Lorem Ipsum is simply dummy text of then of<br>printing and typesetting industry. Lorem</p></div>
<div class="abs service left" style="top:1215px"><h3>Strom Damage</h3><p>Lorem Ipsum is simply dummy text of then of<br>printing and typesetting industry. Lorem</p></div>
<div class="abs service right" style="top:1056px"><h3>Flat Roofs</h3><p>Lorem Ipsum is simply dummy text of then of<br>printing and typesetting industry. Lorem</p></div>
<div class="abs service right" style="top:1136px"><h3>Insurance Work And More</h3><p>Lorem Ipsum is simply dummy text of then of<br>printing and typesetting industry. Lorem</p></div>
<div class="abs service right" style="top:1215px"><h3>Carpentry</h3><p>Lorem Ipsum is simply dummy text of then of<br>printing and typesetting industry. Lorem</p></div>

<div class="abs connector l" style="left:434px;top:1066px"></div>
<div class="abs connector l" style="left:428px;top:1146px"></div>
<div class="abs connector l" style="left:434px;top:1226px"></div>
<div class="abs connector r" style="left:705px;top:1066px"></div>
<div class="abs connector r" style="left:711px;top:1146px"></div>
<div class="abs connector r" style="left:705px;top:1226px"></div>
<div class="abs view-all">View All »</div>

<!-- Projects -->
<div class="abs projects" role="img" aria-label="Suburban street with houses and trees"></div>
<div class="abs projects-veil"></div>
<h2 class="abs heading section-title" style="top:1420px">Our <em>Projects</em></h2>
<span class="abs title-rule" style="left:577px;top:1466px;margin:0"></span>
<div class="abs tabs">
  <span class="on">All</span><span>Shingle Roofs</span><span>Kitchens &amp; Baths</span><span>Strom Damage</span><span>Flat Roofs</span><span>Gutters</span><span>Carpentry</span><span>Roof Repairs</span><span>Windows</span>
</div>

<div class="abs tile" style="left:162px;top:1594px;width:213px;height:191px;background:linear-gradient(160deg,#9fb6c9,#b0593c 45%,#7a3a28)" role="img" aria-label="Roofers working on a tiled roof"><div class="cap">Kitchens &amp; Baths</div></div>
<div class="abs tile feature" style="left:386px;top:1594px;width:426px;height:191px" role="img" aria-label="Chimney on a red tiled roof at dusk"><span class="zoom"></span><div class="label">Roof Repairs</div></div>
<div class="abs tile" style="left:822px;top:1594px;width:214px;height:191px;background:linear-gradient(180deg,#6f95c6,#8a8f90 45%,#5f7a4a)" role="img" aria-label="Large house with shingled roof"><div class="cap">Windows</div></div>
<div class="abs tile" style="left:162px;top:1799px;width:213px;height:191px;background:linear-gradient(180deg,#9bc0de,#4b7b9a 50%,#3c4a52)" role="img" aria-label="Blue house with dormer windows"><div class="cap">Strom Damage</div></div>
<div class="abs tile" style="left:386px;top:1799px;width:209px;height:191px;background:linear-gradient(180deg,#d8e4ee,#a8604a 50%,#5d7a45)" role="img" aria-label="Brick bungalow with tiled roof"><div class="cap">Shingle Roofs</div></div>
<div class="abs tile" style="left:605px;top:1799px;width:207px;height:191px;background:linear-gradient(180deg,#8fb0d4,#8d8578 50%,#6f7d5c)" role="img" aria-label="Two-storey house with grey siding"><div class="cap">Flat Roofs</div></div>
<div class="abs tile" style="left:822px;top:1799px;width:214px;height:191px;background:linear-gradient(160deg,#c5cfd6,#9d9c98 45%,#6b5a4a)" role="img" aria-label="Roofer laying shingles"><div class="cap">Carpentry</div></div>

<!-- Testimonials -->
<div class="abs testimonials" role="img" aria-label="Dark photo of a roofer at work"></div>
<h2 class="abs heading section-title" style="top:2092px;color:var(--white)">Client Testimonials</h2>
<span class="abs title-rule" style="left:577px;top:2138px;margin:0"></span>
<div class="abs arrow" style="left:342px;top:2200px">‹</div>
<div class="abs avatar" style="left:403px;top:2180px;width:76px;height:76px" role="img" aria-label="Client portrait"></div>
<div class="abs avatar" style="left:506px;top:2180px;width:76px;height:76px" role="img" aria-label="Client portrait"></div>
<div class="abs avatar on" style="left:612px;top:2178px;width:80px;height:80px" role="img" aria-label="Client portrait"></div>
<div class="abs avatar" style="left:721px;top:2180px;width:76px;height:76px" role="img" aria-label="Client portrait"></div>
<div class="abs arrow" style="left:842px;top:2200px">›</div>
<div class="abs quote-mark" style="left:122px;top:2266px">“</div>
<p class="abs quote">Lorem Ipsum is simply dummy text of the printing and typesetting industry. Lorem Ipsum has been the industry's standard dummy text ever since the 1500s, when an unknown printer took a galley of type and scrambled it to make a type specimen book. It has survived not only five centuries, but also the leap into electronic typesetting, remaining essentially unchanged. It was popularised in the 1960s with the release.</p>
<div class="abs quote-mark" style="left:790px;top:2318px">”</div>
<div class="abs author">Mr. Lorem Ipsum</div>

<!-- Partners -->
<h2 class="abs heading section-title" style="top:2472px">Our <em>Partner</em></h2>
<span class="abs title-rule" style="left:577px;top:2518px;margin:0"></span>
<div class="abs strip"></div>
<div class="abs strip-shadow"></div>
<div class="abs partner" style="left:250px;top:2614px;width:110px;height:34px;border-radius:4px"></div>
<div class="abs partner" style="left:418px;top:2608px;width:46px;height:46px;border-radius:50%"></div>
<div class="abs partner" style="left:547px;top:2606px;width:56px;height:50px;border-radius:6px"></div>
<div class="abs partner" style="left:700px;top:2612px;width:90px;height:38px;border-radius:4px"></div>
<div class="abs partner" style="left:856px;top:2612px;width:96px;height:38px;border-radius:19px"></div>

<!-- Footer -->
<div class="abs footer"></div>
<div class="abs col" style="left:162px">
  <h4>Navigation</h4>
  <ul><li>Home</li><li>About Us</li><li>Services</li><li>Projects</li><li>Contact Us</li></ul>
</div>
<div class="abs col" style="left:340px;width:240px">
  <h4>Contact Information</h4>
  <div class="contact-line" style="margin-top:18px"><svg width="12" height="14" viewBox="0 0 12 14"><path d="M6 0a5 5 0 0 0-5 5c0 4 5 9 5 9s5-5 5-9a5 5 0 0 0-5-5zm0 7a2 2 0 1 1 0-4 2 2 0 0 1 0 4z" fill="#ddd"/></svg><span>3/79 Lorem Ipsum St, Dolor Amet,<br>New There doni 2222</span></div>
  <div class="contact-line" style="margin-top:16px"><svg width="12" height="12" viewBox="0 0 12 12"><path d="M2.5 0.5l2 2.5-1.2 1.4a7 7 0 0 0 4.3 4.3l1.4-1.2 2.5 2-1 2C5 11.5 0.5 7 0.5 1.5z" fill="#ddd"/></svg><span>312 555 0148 (Ipsum)</span></div>
  <div class="contact-line" style="margin-top:16px"><svg width="12" height="12" viewBox="0 0 12 12"><path d="M2.5 0.5l2 2.5-1.2 1.4a7 7 0 0 0 4.3 4.3l1.4-1.2 2.5 2-1 2C5 11.5 0.5 7 0.5 1.5z" fill="#ddd"/></svg><span>312 555 0192 (Lorem)</span></div>
  <div class="contact-line" style="margin-top:16px"><svg width="13" height="10" viewBox="0 0 13 10"><rect x="0.5" y="0.5" width="12" height="9" fill="none" stroke="#ddd"/><path d="M0.5 0.5l6 5 6-5" fill="none" stroke="#ddd"/></svg><span>hello@brindlecrest-demo.net</span></div>
</div>
<div class="abs col" style="left:609px"><h4>Quick Contact</h4></div>
<div class="field" style="top:2845px;height:24px">Name</div>
<div class="field" style="top:2875px;height:24px">Email</div>
<div class="field" style="top:2903px;height:40px">Message</div>
<div class="abs submit">SUBMIT</div>
<div class="abs col" style="left:850px"><h4>Subscribe</h4></div>
<p class="abs sub-copy">Sign Up for Our Newsletter:<span>Get the word out. Share this page with your friends and family. Enter your email address...</span></p>
<div class="abs sub-input"></div>
<div class="abs sub-go">GO</div>

<div class="abs bottombar"></div>
<p class="abs copyright">Copyright 2016 Brindlecrest Roofing Construction. All Rights Reserved.</p>
<span class="abs social" style="left:925px"></span>
<span class="abs social" style="left:954px"></span>
<span class="abs social" style="left:984px"></span>
<span class="abs social" style="left:1014px"></span>

</body>
</html>
```